Health & Fitness Author & Public Speaker Needs Visually Stunning Web Design!

We've FINALLY got around to launching a website for Belinda Marchetti - Australian Food Coach and Health & Fitness Expert. The website is to promote her new healthy eating program - "Bright Plate Living".
For a compehensive outline of exactly what we are after, please see the following attached files:
(1) Web Layout (wireframe, content/copy, links to photos to use, sample page we love)
(2) Style Guide (these are the colours, and overall feel we want)
Photos that we'd like used (of Belinda, and food/meals) can be found at these URL's:
Profile: https://www.filecrate.example/sh/q4r8vpl2m7xz/K3tPzWq9Lm
PicVault: https://www.filecrate.example/sh/b7nwe3ju1kd5/9hFrTy2Qxa
HINT:
Before you do ANYTHING - check out this site as it is pretty much EXACTLY what we're after, but with our branding/colours/style: http://tessamorrow.example/
As we will need to revamp our existing Chatterbook page & other printed material, there may be the potential for further work for the successful designer in the future.
Thanks & Good Luck!
Donovan Pryle
Marketing & Business Development Manager
Bright Plate Living
Women, Ages 24 - 45, Interested in Healthly Eating & Fitness
Business

```html
<!DOCTYPE html>
<html lang="en">
<head>
<meta charset="utf-8">
<title>Bright Plate Living — Belinda Marchetti</title>
<link rel="stylesheet" href="https://fonts.googleapis.com/css2?family=Ubuntu:wght@400;500;700&family=Roboto+Condensed:wght@700&family=Arimo:wght@400;700&display=swap">
<style>
:root{
  --pink:#e8175d;
  --pink-deep:#c8104c;
  --purple:#9b1aa6;
  --charcoal:#2e2e30;
  --ink:#1f1f1f;
  --muted:#8a8a8a;
  --body:#4a4a4a;
  --line:#d6d6d6;
  --paper:#ffffff;
  --mist:#f3f3f3;
}
*{margin:0;padding:0;box-sizing:border-box}
html,body{width:1084px;height:1200px;overflow:hidden;background:var(--paper)}
body{font-family:"Arimo",Arial,sans-serif;color:var(--body)}
.page{position:relative;width:1084px;height:1200px;overflow:hidden;background:var(--paper)}
.abs{position:absolute}

/* hero */
.hero-photo{left:0;top:0;width:1084px;height:496px;
  background:
    radial-gradient(ellipse 200px 250px at 590px 300px, rgba(110,100,92,.55), rgba(110,100,92,0) 70%),
    radial-gradient(ellipse 120px 90px at 780px 380px, rgba(235,235,232,.55), rgba(235,235,232,0) 70%),
    radial-gradient(ellipse 260px 150px at 1010px 150px, rgba(242,240,228,.9), rgba(242,240,228,0) 72%),
    radial-gradient(ellipse 420px 230px at 190px 150px, rgba(62,92,44,.8), rgba(62,92,44,0) 72%),
    radial-gradient(ellipse 360px 160px at 560px 120px, rgba(80,110,52,.6), rgba(80,110,52,0) 72%),
    linear-gradient(180deg,#dfe6d6 0%,#a9bd86 22%,#7a9a4c 48%,#6e8f3f 66%,#86a050 84%,#99a96a 100%)}
.topbar{left:0;top:0;width:1084px;height:44px;background:linear-gradient(180deg,#ffffff,#ececec);box-shadow:0 2px 4px rgba(0,0,0,.15)}
.brand{left:179px;top:0;width:274px;height:131px;background:linear-gradient(180deg,#fbfbfb,#ededed);box-shadow:0 2px 6px rgba(0,0,0,.25);
  display:flex;align-items:center;justify-content:center}
.brand-name{font-family:"Ubuntu",sans-serif;font-weight:500;font-size:30px;line-height:1.05;color:var(--pink);text-align:center;letter-spacing:-.5px}
.nav{left:548px;top:9px;display:flex;gap:14px;font-family:"Ubuntu",sans-serif;font-weight:700;font-size:16px;color:var(--charcoal)}
.nav a{color:inherit;text-decoration:none;padding:5px 12px;border-radius:14px}
.nav a.current{color:var(--pink);background:#fff;box-shadow:0 0 4px rgba(0,0,0,.12)}

.tag{font-family:"Ubuntu",sans-serif;font-weight:700;color:#fff;text-align:center;line-height:1;white-space:nowrap;overflow:hidden}
.tag-slim{left:252px;top:196px;width:201px;height:50px;background:var(--pink);font-size:44px;padding-top:3px;letter-spacing:-.5px}
.tag-energy{left:137px;top:252px;width:316px;height:47px;background:var(--purple);font-size:40px;padding-top:3px;letter-spacing:-1px}
.tag-guilt{left:208px;top:305px;width:245px;height:44px;background:var(--charcoal);font-size:40px;padding-top:2px;letter-spacing:-.5px}
.tag-with{left:208px;top:357px;width:245px;height:20px;background:var(--pink);font-size:15px;padding-top:2px;font-weight:500}

.by{left:714px;top:155px;font-family:"Ubuntu",sans-serif;font-size:20px;color:var(--pink);letter-spacing:2px}
.name-first{left:710px;top:186px;height:29px;padding:0 8px 0 2px;background:#fff;font-family:"Ubuntu",sans-serif;font-weight:500;font-size:29px;line-height:29px;color:var(--pink);letter-spacing:1px}
.name-last{left:708px;top:219px;height:31px;padding:0 4px;background:var(--charcoal);font-family:"Ubuntu",sans-serif;font-weight:500;font-size:29px;line-height:31px;color:#fff;letter-spacing:1px}
.featured{left:708px;top:462px;width:222px;height:29px;background:#fff;font-family:"Ubuntu",sans-serif;font-size:15px;line-height:29px;color:var(--pink);padding-left:12px}
.featured b{color:var(--ink);font-weight:700;font-size:17px;margin-left:6px}
.dots{left:165px;top:453px;display:flex;gap:3px}
.dots span{width:10px;height:10px;border:2px solid #fff;background:rgba(255,255,255,.25)}
.dots span.on{background:var(--pink)}

/* signup band */
.band{left:0;top:496px;width:1084px;height:80px;background:linear-gradient(180deg,#ee2a6a,var(--pink-deep));border-bottom:3px solid #8e0b35}
.band-title{left:152px;top:508px;font-family:"Ubuntu",sans-serif;font-weight:500;color:#fff;line-height:1}
.band-title .small{font-size:14px;display:block}
.band-title .big{font-size:19px;display:block;letter-spacing:-.6px;margin-top:3px}
.band-blurb{left:364px;top:511px;width:112px;font-size:9.5px;font-weight:700;color:#fff;text-align:center;line-height:12.5px}
.mail-icon{left:481px;top:521px}
.field{background:#fff;border:1px solid #d9d9d9;border-radius:2px;font-size:9.5px;color:#555;padding-left:7px;line-height:25px;height:26px}
.f-first{left:513px;top:523px;width:141px}
.f-email{left:657px;top:523px;width:166px}
.hook{left:827px;top:523px;width:103px;height:26px;background:var(--charcoal);border-radius:3px;color:#fff;font-family:"Ubuntu",sans-serif;font-weight:700;font-size:11px;display:flex;align-items:center;justify-content:space-between;padding:0 5px}

/* posts */
.post-img{width:137px;height:138px;border:4px solid #e6e6e6;box-shadow:0 0 0 1px #cfcfcf}
.img-salad{background:linear-gradient(135deg,#f2f4ec,#9cc25a 45%,#d9a55a 70%,#eceee6)}
.img-juice{background:linear-gradient(135deg,#e9f0d5,#c7dc8e 45%,#6aa534 75%,#f3f6ee)}
.img-tomato{background:linear-gradient(135deg,#e8d6b0,#d63a22 40%,#7a4a2a 70%,#c43c3c)}
.post-title{font-size:13.5px;color:var(--ink);font-family:"Arimo",sans-serif}
.post-meta{font-size:9px;color:var(--muted);margin-top:6px}
.post-text{width:343px;font-size:10.6px;line-height:16.5px;margin-top:8px;color:var(--body)}
.post-text b{color:var(--pink)}
.more{display:inline-block;margin-top:13px;background:var(--pink);color:#fff;font-family:"Roboto Condensed",sans-serif;font-weight:700;font-size:13px;padding:3px 12px;letter-spacing:-.2px}

/* sidebar */
.ad{left:695px;width:235px;border:2px solid var(--pink)}
.ad-book{top:588px;height:192px}
.ad-book .photo{position:absolute;inset:0;background:linear-gradient(100deg,#b8ab9d 0%,#d8ccc0 45%,#f4eef0 62%,#e7b9d4 100%)}
.lbl{position:absolute;right:4px;font-family:"Ubuntu",sans-serif;font-weight:700;color:#fff;font-size:11px;padding:1px 5px;white-space:nowrap}
.lbl.pink{background:var(--pink)}
.lbl.dark{background:var(--charcoal)}
.lbl.purple{background:var(--purple)}
.ad-challenge{top:794px;height:193px;background:linear-gradient(180deg,#d9a86e,#e8d3b0 40%,#7e8a3e 70%,#c9a24f)}
.ch-title{position:absolute;left:6px;top:5px;width:222px;height:30px;background:var(--pink);font-family:"Ubuntu",sans-serif;font-weight:500;font-size:19px;color:#fff;line-height:30px;padding-left:14px}
.ch-sub{position:absolute;left:6px;top:39px;width:222px;height:18px;background:var(--charcoal);font-family:"Ubuntu",sans-serif;font-weight:700;font-size:10.5px;color:#fff;line-height:18px;padding-left:8px}
.join-box{left:695px;top:1003px;width:235px;height:118px;border:1px solid #cfcfcf;background:#fff;padding:9px 12px}
.join-box h3{font-family:"Ubuntu",sans-serif;font-weight:700;font-size:12px;color:var(--ink);letter-spacing:.3px}
.join-box p{font-size:8.5px;line-height:14px;margin-top:5px;color:#444}
.jf{position:absolute;left:9px;width:153px;height:23px;background:linear-gradient(180deg,#f2f2f2,#fff);border:1px solid #e1e1e1;font-size:9px;line-height:22px;padding-left:10px;color:#444}
.signup{position:absolute;left:168px;top:62px;width:58px;height:50px;background:var(--pink);color:#fff;font-family:"Roboto Condensed",sans-serif;font-weight:700;font-size:12px;display:flex;align-items:center;justify-content:center;box-shadow:0 0 0 2px #eee}

/* footer */
.foot{left:0;top:1138px;width:1084px;height:55px;background:linear-gradient(180deg,#fafafa,#ececec);border-top:1px solid #dcdcdc;border-bottom:1px solid #dcdcdc}
.foot-links{left:163px;top:1156px;font-family:"Roboto Condensed",sans-serif;font-weight:700;font-size:17px;color:var(--charcoal);letter-spacing:-.4px}
.foot-links i{font-style:normal;color:var(--pink);margin:0 6px;font-weight:400}
.follow{left:620px;top:1158px;font-family:"Roboto Condensed",sans-serif;font-weight:700;font-size:15px;color:var(--charcoal);display:flex;align-items:center;gap:9px}
.social{display:flex;align-items:center;gap:4px;font-family:"Arimo",sans-serif;font-weight:700;font-size:10px;color:var(--charcoal)}
.social::before{content:"";width:10px;height:10px;border-radius:50%;background:var(--pink)}
</style>
</head>
<body>
<div class="page">

  <div class="abs hero-photo" role="img" aria-label="Photo of Belinda sitting cross-legged on park grass with a water bottle, an apple and boxing gloves, trees and a pale building behind"></div>
  <div class="abs topbar"></div>
  <div class="abs brand"><div class="brand-name">Bright Plate<br>Living</div></div>
  <nav class="abs nav">
    <a class="current" href="#">HOME</a><a href="#">ABOUT</a><a href="#">THE PLAN</a><a href="#">SHOP</a>
  </nav>

  <div class="abs tag tag-slim">GET SLIM</div>
  <div class="abs tag tag-energy">BOOST ENERGY</div>
  <div class="abs tag tag-guilt">GUILT FREE</div>
  <div class="abs tag tag-with">WITH BRIGHT PLATE LIVING!</div>

  <div class="abs by">BY</div>
  <div class="abs name-first">BELINDA</div>
  <div class="abs name-last">MARCHETTI</div>
  <div class="abs featured">Featured in<b>Verity Mode</b></div>
  <div class="abs dots"><span class="on"></span><span></span><span></span><span></span></div>

  <div class="abs band"></div>
  <div class="abs band-title"><span class="small">Join the</span><span class="big">BRIGHT PLATE LIVING</span><span class="big">Movement</span></div>
  <div class="abs band-blurb">Get a weekly serving of inspiration &amp; advice that will change your life...bring it on!</div>
  <svg class="abs mail-icon" width="28" height="28" viewBox="0 0 28 28" aria-hidden="true">
    <circle cx="14" cy="14" r="13" fill="none" stroke="#fff" stroke-width="1.5" opacity=".7"/>
    <rect x="7.5" y="9.5" width="13" height="9" rx="1" fill="none" stroke="#fff" stroke-width="1.3"/>
    <path d="M7.5 10l6.5 5 6.5-5" fill="none" stroke="#fff" stroke-width="1.3"/>
  </svg>
  <div class="abs field f-first">Your First Name</div>
  <div class="abs field f-email">Your Email Address</div>
  <div class="abs hook">HOOK ME UP!
    <svg width="18" height="18" viewBox="0 0 18 18" aria-hidden="true"><circle cx="9" cy="9" r="8" fill="var(--pink)" stroke="#fff" stroke-width="1.2"/><path d="M7.5 5.5L11 9l-3.5 3.5" fill="none" stroke="#fff" stroke-width="1.8"/></svg>
  </div>

  <div class="abs post-img img-salad" style="left:156px;top:607px" role="img" aria-label="Fresh green salad with croutons"></div>
  <div class="abs" style="left:307px;top:607px">
    <div class="post-title">Eating Plans, Advice and Expert Tips</div>
    <div class="post-meta">December 3, 2012 by Editor</div>
    <div class="post-text"><b>Lorem ipsum dolor sit amet,</b> consectetuer adipiscing elit, sed diam nonummy nibh euismod tincidunt ut laoreet dolore magna aliquam erat volutpat. Ut wisi enim ad minim veniam, quis nostrud exerci tation ullamcorper suscipit lobortis isl ut aliquip ex ea commodo.</div>
    <span class="more">READ MORE</span>
  </div>

  <div class="abs post-img img-juice" style="left:156px;top:770px" role="img" aria-label="Green smoothie in a glass beside fresh chives"></div>
  <div class="abs" style="left:307px;top:770px">
    <div class="post-title">Eating Plans, Advice and Expert Tips</div>
    <div class="post-meta">December 3, 2012 by Editor</div>
    <div class="post-text"><b>Lorem ipsum dolor sit amet,</b> consectetuer adipiscing elit, sed diam nonummy nibh euismod tincidunt ut laoreet dolore magna aliquam erat volutpat. Ut wisi enim ad minim veniam, quis nostrud exerci tation ullamcorper suscipit lobortis isl ut aliquip ex ea commodo.</div>
    <span class="more">READ MORE</span>
  </div>

  <div class="abs post-img img-tomato" style="left:156px;top:942px" role="img" aria-label="Tomatoes, oil and peppercorns in a wooden bowl"></div>
  <div class="abs" style="left:307px;top:942px">
    <div class="post-title">Eating Plans, Advice and Expert Tips</div>
    <div class="post-meta">December 3, 2012 by Editor</div>
    <div class="post-text"><b>Lorem ipsum dolor sit amet,</b> consectetuer adipiscing elit, sed diam nonummy nibh euismod tincidunt ut laoreet dolore magna aliquam erat volutpat. Ut wisi enim ad minim veniam, quis nostrud exerci tation ullamcorper suscipit lobortis isl ut aliquip ex ea commodo.</div>
    <span class="more">READ MORE</span>
  </div>

  <div class="abs ad ad-book">
    <div class="photo" role="img" aria-label="Photo of Belinda against a stone wall beside the eating plan book cover"></div>
    <span class="lbl pink" style="top:120px">The Ultimate</span>
    <span class="lbl dark" style="top:138px">BRIGHT PLATE LIVING Guide</span>
    <span class="lbl pink" style="top:157px">By Belinda Marchetti</span>
    <span class="lbl purple" style="top:175px">Get Yours Now! ►</span>
  </div>

  <div class="abs ad ad-challenge" role="img" aria-label="Bowl of rice with beef, broccoli and peppers on a bamboo mat">
    <div class="ch-title">12 WEEK CHALLENGE</div>
    <div class="ch-sub">Healthy, Happy &amp; Hot In No Time Flat!</div>
    <span class="lbl purple" style="top:174px">Join Us Now! ►</span>
  </div>

  <div class="abs join-box">
    <h3>JOIN THE MOVEMENT!</h3>
    <p>Join the Bright Plate Living Movement and get a free copy of The Kick Start Plan (valued $27.00)!</p>
    <div class="jf" style="top:62px">Name</div>
    <div class="jf" style="top:89px">Email</div>
    <div class="signup">SIGN UP!</div>
  </div>

  <div class="abs foot"></div>
  <div class="abs foot-links">COMMUNITY<i>/</i>FREE RESOURCES<i>/</i>PRESS<i>/</i>CONTACT</div>
  <div class="abs follow">FOLLOW AT
    <span class="social">Chatterbook</span>
    <span class="social">Chirpline</span>
    <span class="social">Reelhouse</span>
    <span class="social">Pinboardly</span>
  </div>

</div>
</body>
</html>
```